Recruiting agency looking for a newsletter design

We need to design a newsletter that will be sent by e-mail to our clients database. This communication announces a new milestone for our company.

We need it to convey high professionalism, elegance ad luxury. It needs to catch the reader’s attention.

The background needs to be light shiny silver, not flat gray, not dark silver. Some effects can give dimension to the content. We need a very impactful communication.

You will find attached:

- The content that needs to appear on the newsletter
- Pictures “moodboard” that you can take into consideration for the overall “atmosphere” and “emotion” that the design needs to convey. Please DO NOT include any of these images in the newsletter itself. They are just here to help you get the idea of the type of image we want to convey as a company with this communication.
- Company logo
- Please note that I will provide you later on with a URL link to include to the newsletter.

```html
<!DOCTYPE html>
<html lang="en">
<head>
<meta charset="utf-8">
<title>2021 New Era – New Fees</title>
<link rel="stylesheet" href="https://fonts.googleapis.com/css2?family=Montserrat:wght@400;500;600;700;800&display=swap">
<style>
  :root{
    --navy:#1b2452;
    --navy-deep:#141b40;
    --pink:#e5245a;
    --silver-light:#e9eaee;
    --silver:#c9cbd1;
    --white:#ffffff;
    --ink:#333333;
  }
  *{box-sizing:border-box;margin:0;padding:0}
  html,body{width:683px;height:1200px;overflow:hidden;background:var(--white);font-family:"Montserrat",Arial,sans-serif}
  .preheader{position:absolute;top:30px;left:0;width:683px;text-align:center;font-size:10.5px;line-height:15px;color:var(--ink)}
  .preheader a{color:var(--pink);text-decoration:underline}
  .newsletter{position:absolute;left:130px;top:84px;width:421px;height:872px;border-radius:10px;
    background:linear-gradient(180deg,var(--silver) 0%,#dcdde2 60%,var(--silver-light) 100%);padding:9px}
  .sheet{position:relative;width:100%;height:100%;border-radius:4px;overflow:hidden;
    background:linear-gradient(160deg,#f4f5f7 0%,#d9dbe0 45%,#f2f3f5 70%,#cfd1d6 100%)}
  .masthead{position:absolute;left:0;top:0;width:100%;height:174px;background:var(--white);text-align:center}
  .year{padding-top:30px;font-size:68px;font-weight:800;color:var(--navy);letter-spacing:1px;line-height:70px}
  .era{margin-top:18px;font-size:20px;font-weight:700;color:var(--navy)}
  .era span{color:var(--pink)}
  .panel{position:absolute;left:0;top:174px;width:100%;height:622px}
  .panel svg.bg{position:absolute;left:0;top:0}
  .hex{position:absolute}
  .hex-meeting{left:52px;top:48px}
  .hex-car{left:222px;top:178px}
  .stat{position:absolute;color:var(--white);text-align:center}
  .stat .label{font-size:14px;font-weight:600;line-height:17px}
  .stat .value{font-size:44px;font-weight:800;line-height:50px}
  .stat-other{left:218px;top:54px;width:140px}
  .stat-top{left:56px;top:186px;width:140px}
  .cta{position:absolute;left:0;top:398px;width:100%;text-align:center;color:var(--white)}
  .cta h2{font-size:22px;font-weight:600;line-height:27px}
  .cta h2 em{font-style:normal;font-weight:800;color:var(--pink)}
  .cta .more{margin-top:20px;display:flex;justify-content:center;align-items:center;gap:16px;font-size:13px;font-weight:600}
  .button{display:inline-block;background:var(--pink);color:var(--white);border-radius:16px;padding:8px 20px;font-size:12px;font-weight:700;text-decoration:none}
  .brand{position:absolute;left:0;top:806px;width:100%;text-align:center;color:var(--ink)}
  .brand-name{display:inline-flex;align-items:center;gap:8px;font-size:18px;font-weight:700;color:#3a3a3a}
  .brand-name i{display:inline-block;width:10px;height:10px;background:#3a3a3a}
  .brand-tag{margin-top:4px;font-size:10px;font-weight:500;color:#555555}
</style>
</head>
<body>
  <p class="preheader">Is this email not displaying correctly?<br><a href="#">View it in your browser.</a></p>

  <main class="newsletter">
    <div class="sheet">
      <header class="masthead">
        <h1 class="year">2021</h1>
        <p class="era">NEW ERA - <span>(NEW FEES)</span></p>
      </header>

      <section class="panel">
        <svg class="bg" width="403" height="622" viewBox="0 0 403 622">
          <defs>
            <radialGradient id="panelGlow" cx="0.45" cy="0.35" r="0.7">
              <stop offset="0" stop-color="#26306a"/>
              <stop offset="1" stop-color="#161d45"/>
            </radialGradient>
          </defs>
          <polygon points="0,0 403,0 403,518 201,621 0,518" fill="url(#panelGlow)"/>
        </svg>

        <svg class="hex hex-meeting" width="140" height="140" viewBox="0 0 140 140" role="img" aria-label="Photo of a business meeting with hands over documents">
          <defs>
            <linearGradient id="meetFill" x1="0" y1="0" x2="1" y2="1">
              <stop offset="0" stop-color="#8f96b5"/>
              <stop offset="0.5" stop-color="#cfd2de"/>
              <stop offset="1" stop-color="#5a5f7d"/>
            </linearGradient>
          </defs>
          <polygon points="70,4 131,36 131,104 70,136 9,104 9,36" fill="url(#meetFill)" stroke="#e5245a" stroke-width="4"/>
        </svg>

        <svg class="hex hex-car" width="160" height="160" viewBox="0 0 150 150" role="img" aria-label="Photo of a luxury car in a showroom">
          <defs>
            <linearGradient id="carFill" x1="0" y1="0" x2="0" y2="1">
              <stop offset="0" stop-color="#d9dadd"/>
              <stop offset="0.55" stop-color="#7a7c82"/>
              <stop offset="1" stop-color="#aeb0b5"/>
            </linearGradient>
          </defs>
          <polygon points="75,4 140,40 140,110 75,146 10,110 10,40" fill="url(#carFill)" stroke="#ffffff" stroke-width="4"/>
        </svg>

        <div class="stat stat-other">
          <p class="label">All other<br>appointments</p>
          <p class="value">21%</p>
        </div>
        <div class="stat stat-top">
          <p class="label">Top managers<br>Executives</p>
          <p class="value">50%</p>
        </div>

        <div class="cta">
          <h2><em>JOIN US</em> in shaping the future<br>of recruitment</h2>
          <p class="more">For more information <a class="button" href="#">Click Here</a></p>
        </div>
      </section>

      <footer class="brand">
        <p class="brand-name"><i></i>Meridian Talent</p>
        <p class="brand-tag">Life sciences recruitment worldwide</p>
      </footer>
    </div>
  </main>
</body>
</html>
```